2026 Wall Calendar Design - 11" x 8.5"

You created the design for our 2025 calendar and we're hoping to work with you again on the calendar for 2026.

This is the template for the calendar - https://apps.moxlaprint.com/products/product/4627#tab__product-templates

Type: Wall Calendar
Binding: Wire - O
Printing: Double sided (Hero shot on one side and dates on the other.)
Measurement: 11.00 in wide x 8.50 in tall (US)
Orientation: Landscape
Color: Full color
Printing Process: Toner (TNR)

This is what we'd like to begin with for the design:

1. Outside front cover
2. Outside back cover
3. Inside front cover
4. Inside back cover
5. Two example calendar months:
one with 5 weeks (Jan 2026)
one with 6 weeks (Feb 2026)

On the example calendar month, previous and next months calendar boxes should be different than the current calendar month boxes.

The calendar boxes have to be big enough to put the info for the holidays and special days that's in the spreadsheet.

Photos can be found here: https://www.velnishare.com/scl/fo/q4rtwp8bn2xkc0vjh5ez3/KxRtP9wqmbzLvTnQeY24Hc7?rlkey=t5bwq8zn2vkfyra0hdl3ceu6m&st=8kq71vxe&dl=0

```html
<!DOCTYPE html>
<html lang="en">
<head>
<meta charset="utf-8">
<title>Heartland Tales 2026 Calendar</title>
<link href="https://fonts.googleapis.com/css2?family=Audiowide&family=Open+Sans:wght@600;700;800&family=Rubik+Dirt&display=swap" rel="stylesheet">
<style>
  :root{
    --red:#c1272d;
    --red-dark:#8e1b20;
    --blue:#1f3a6e;
    --blue-dark:#14264b;
    --cell:#eeeeee;
    --ink:#1b1b1b;
    --paper:#ffffff;
    --tear:#e4e4e4;
  }
  *{box-sizing:border-box;margin:0;padding:0}
  html,body{width:1200px;height:997px;overflow:hidden;background:var(--paper)}
  body{position:relative;font-family:"Open Sans",sans-serif}

  .sheet{position:absolute;width:510px;height:394px;background:var(--paper);
    box-shadow:6px 10px 18px rgba(0,0,0,.28);overflow:hidden}
  .sheet--photo-top{left:64px;top:63px}
  .sheet--cal-top{left:625px;top:63px}
  .sheet--photo-bottom{left:64px;top:540px}
  .sheet--cal-bottom{left:625px;top:540px}

  /* photo side */
  .hero{position:absolute;inset:0}
  .hero--range{background:linear-gradient(135deg,#6b6a4c 0%,#8b8463 35%,#5d6b3c 65%,#3e4a2a 100%)}
  .hero--river{background:linear-gradient(160deg,#9a938a 0%,#7f7a70 40%,#6c6a55 70%,#524d3e 100%)}
  .quote-band{position:absolute;left:0;top:282px;width:482px;height:92px;
    clip-path:polygon(0 8%,6% 3%,12% 9%,18% 2%,25% 7%,32% 1%,40% 8%,48% 3%,56% 9%,63% 2%,71% 6%,78% 0,86% 7%,93% 2%,96% 10%,94% 25%,98% 40%,95% 55%,99% 70%,96% 86%,90% 94%,82% 98%,74% 93%,66% 100%,57% 95%,48% 100%,39% 94%,30% 99%,20% 93%,10% 98%,0 94%);
    display:flex;align-items:center;justify-content:space-between;padding:0 44px 0 19px}
  .quote-band--blue{background:radial-gradient(ellipse at 40% 50%,#27498a 0%,var(--blue) 55%,var(--blue-dark) 100%)}
  .quote-band--red{background:radial-gradient(ellipse at 40% 50%,#d2333a 0%,var(--red) 55%,var(--red-dark) 100%)}
  .quote{color:#fff;font-weight:700;font-size:9.4px;line-height:13px;text-transform:uppercase;width:300px}
  .brand{display:flex;align-items:center;gap:5px;font-weight:800;font-size:11px;line-height:11px;text-transform:uppercase;letter-spacing:.3px}
  .brand__dot{width:10px;height:10px;border-radius:50%}
  .brand--light{color:#fff}
  .brand--light .brand__dot{background:#fff}
  .brand--dark{color:var(--blue)}
  .brand--dark .brand__dot{background:var(--red)}

  /* calendar side */
  .tear-shadow{position:absolute;left:0;top:0;width:140px;height:394px;background:var(--tear);
    clip-path:polygon(0 0,90% 0,98% 4%,93% 9%,99% 14%,94% 20%,100% 27%,95% 33%,100% 40%,96% 47%,100% 54%,94% 61%,99% 68%,93% 75%,98% 82%,92% 89%,96% 95%,89% 100%,0 100%)}
  .sidebar{position:absolute;left:0;top:0;width:135px;height:394px;
    clip-path:polygon(0 0,88% 0,95% 4%,90% 9%,96% 14%,91% 20%,97% 27%,92% 33%,98% 40%,93% 47%,97% 54%,91% 61%,96% 68%,90% 75%,95% 82%,89% 89%,93% 95%,86% 100%,0 100%)}
  .sidebar--red{background:linear-gradient(90deg,#b82329 0%,var(--red) 70%,#a51f24 100%)}
  .sidebar--blue{background:linear-gradient(90deg,#1a3263 0%,var(--blue) 70%,#183060 100%)}
  .month{position:absolute;left:14px;top:32px;width:74px;text-align:center;color:#fff;
    font-family:"Audiowide",sans-serif;font-size:32px;line-height:38px}
  .month-rule{position:absolute;left:14px;top:77px;width:74px;height:1px;background:rgba(255,255,255,.8)}
  .year{position:absolute;left:22px;top:112px;width:60px;height:214px;color:#fff;
    font-family:"Rubik Dirt",sans-serif;font-size:58px;line-height:60px;letter-spacing:-2px;
    writing-mode:vertical-rl;transform:rotate(180deg);text-align:center}

  .weekdays{position:absolute;left:155px;top:43px;display:grid;grid-template-columns:repeat(7,44px);column-gap:4.6px}
  .weekday{font-family:"Audiowide",sans-serif;font-size:17px;color:var(--blue);text-align:center}
  .weekday--sun{color:var(--red)}
  .days{position:absolute;left:155px;top:74px;display:grid;grid-template-columns:repeat(7,44px);
    grid-auto-rows:44px;column-gap:4.6px;row-gap:4px}
  .day{background:var(--cell);font-weight:700;font-size:11px;color:var(--ink);text-align:right;padding:4px 6px 0 0}
  .day--mark{color:var(--red)}
  .day--blank{visibility:hidden}

  .cal-footer{position:absolute;left:150px;top:346px;width:220px;text-align:right;color:var(--blue);
    font-weight:600;font-size:7.2px;line-height:11px}
  .cal-brand{position:absolute;left:384px;top:350px}
</style>
</head>
<body>

  <section class="sheet sheet--photo-top">
    <div class="hero hero--range" role="img" aria-label="Photo: marksman in camo hat and ear protection aiming a scoped rifle in a forest"></div>
    <div class="quote-band quote-band--blue">
      <p class="quote">“If you fail to plan, you plan to fail. It’s that simple. Nothing ever goes 100% according to plan, but being prepared make all the difference”</p>
      <div class="brand brand--light"><span class="brand__dot"></span><span>Heartland<br>Tales</span></div>
    </div>
  </section>

  <section class="sheet sheet--cal-top">
    <div class="tear-shadow"></div>
    <div class="sidebar sidebar--red">
      <div class="month">JUN</div>
      <div class="month-rule"></div>
      <div class="year">2026</div>
    </div>
    <div class="weekdays">
      <span class="weekday weekday--sun">SU</span><span class="weekday">MO</span><span class="weekday">TU</span><span class="weekday">WE</span><span class="weekday">TH</span><span class="weekday">FR</span><span class="weekday">SA</span>
    </div>
    <div class="days">
      <span class="day day--blank"></span><span class="day day--blank"></span><span class="day day--blank"></span><span class="day day--blank"></span>
      <span class="day">1</span><span class="day">2</span><span class="day">3</span>
      <span class="day day--mark">4</span><span class="day">5</span><span class="day">6</span><span class="day">7</span><span class="day">8</span><span class="day">9</span><span class="day">10</span>
      <span class="day day--mark">11</span><span class="day">12</span><span class="day">13</span><span class="day">14</span><span class="day">15</span><span class="day">16</span><span class="day">17</span>
      <span class="day day--mark">18</span><span class="day">19</span><span class="day">20</span><span class="day">21</span><span class="day">22</span><span class="day">23</span><span class="day">24</span>
      <span class="day day--mark">25</span><span class="day">26</span><span class="day">27</span><span class="day">28</span><span class="day">29</span><span class="day">30</span><span class="day">31</span>
    </div>
    <p class="cal-footer">Stories About Life - Stories That Inspire - Stories About You<br>www.heartlandtales.tv</p>
    <div class="brand brand--dark cal-brand"><span class="brand__dot"></span><span>Heartland<br>Tales</span></div>
  </section>

  <section class="sheet sheet--photo-bottom">
    <div class="hero hero--river" role="img" aria-label="Photo: two anglers in waders fly fishing in a rocky river"></div>
    <div class="quote-band quote-band--red">
      <p class="quote">“If you fail to plan, you plan to fail. It’s that simple. Nothing ever goes 100% according to plan, but being prepared make all the difference”</p>
      <div class="brand brand--light"><span class="brand__dot"></span><span>Heartland<br>Tales</span></div>
    </div>
  </section>

  <section class="sheet sheet--cal-bottom">
    <div class="tear-shadow"></div>
    <div class="sidebar sidebar--blue">
      <div class="month">FEB</div>
      <div class="month-rule"></div>
      <div class="year">2026</div>
    </div>
    <div class="weekdays">
      <span class="weekday weekday--sun">SU</span><span class="weekday">MO</span><span class="weekday">TU</span><span class="weekday">WE</span><span class="weekday">TH</span><span class="weekday">FR</span><span class="weekday">SA</span>
    </div>
    <div class="days">
      <span class="day">1</span><span class="day">2</span><span class="day">3</span><span class="day day--mark">4</span><span class="day">5</span><span class="day">6</span><span class="day">7</span>
      <span class="day">8</span><span class="day">9</span><span class="day">10</span><span class="day day--mark">11</span><span class="day">12</span><span class="day">13</span><span class="day">14</span>
      <span class="day">15</span><span class="day">16</span><span class="day">17</span><span class="day day--mark">18</span><span class="day">19</span><span class="day">20</span><span class="day">21</span>
      <span class="day">22</span><span class="day">23</span><span class="day">24</span><span class="day day--mark">25</span><span class="day">26</span><span class="day">27</span><span class="day">28</span>
    </div>
    <p class="cal-footer">Stories About Life - Stories That Inspire - Stories About You<br>www.heartlandtales.tv</p>
    <div class="brand brand--dark cal-brand"><span class="brand__dot"></span><span>Heartland<br>Tales</span></div>
  </section>

</body>
</html>
```